Carpal Tunnel - PPC Landing Page

We need to do a SINGLE page landing page for a doctor who specializes in Carpal Tunnel syndrome - please research if you're not familiar - it's very common.

Landing page essentials:
Must have a form in upper right hand corner:
Form title: "Get a free diagnosis."
Form inputs: Name, Phone, Email, Requested Appointment time

Page is for PPC, so needs to be simple and light on content. Content has been provided and attached to this project.

No navigation, just a single page.

Industry/Entity Type

Health

Coding

Coded - Design and coding required

Number of Pages Required

1 page

Requirements
Must have
• Elegant look - Conversion optimized for form and phone
• Responsive design.
Should not have
• Old outdated images.

```html
<!DOCTYPE html>
<html lang="en">
<head>
<meta charset="utf-8">
<title>Dr. Marlowe – Carpal Tunnel Care</title>
<link href="https://fonts.googleapis.com/css2?family=Open+Sans:wght@400;600;700&display=swap" rel="stylesheet">
<style>
:root{
  --teal:#3ea6b6;
  --teal-dark:#2f8d9c;
  --green:#3dba7d;
  --green-dark:#2fa56b;
  --page:#ecebe6;
  --ink:#5b6166;
  --muted:#8d9296;
  --footer:#2d545e;
  --footer-deep:#23444c;
  --white:#ffffff;
}
*{box-sizing:border-box;margin:0;padding:0}
html,body{width:878px;height:1200px;overflow:hidden}
body{background:var(--page);font-family:"Open Sans",Arial,sans-serif;color:var(--ink);font-size:11px;position:relative}

.topbar{height:40px;background:var(--teal);display:flex;align-items:center;justify-content:space-between;padding:0 130px}
.brand{color:var(--white);font-weight:700;font-size:15px;letter-spacing:.5px}
.top-phone{color:var(--white);font-size:11px;display:flex;align-items:center;gap:6px}

.hero{position:relative;height:256px;width:878px}
.hero-photo{position:absolute;inset:0;background:linear-gradient(100deg,#f2f4f5 0%,#dfe6ea 22%,#9fb3be 40%,#c7b3a5 60%,#8f8a86 100%)}
.lead-form{position:absolute;right:130px;top:38px;width:140px;background:var(--white);border:2px solid var(--green);padding:6px 8px 8px}
.lead-form h2{font-size:9px;font-weight:600;color:var(--teal);margin-bottom:6px}
.field{display:flex;align-items:center;margin-bottom:7px}
.field label{width:34px;font-size:7px;color:var(--ink)}
.field span{flex:1;height:12px;border:1px solid #cfd3d6}
.submit{display:block;margin-left:auto;background:var(--green);color:var(--white);font-size:7px;padding:3px 8px;border:0}

.tabs{height:30px;background:var(--green);display:flex;justify-content:center}
.tabs div{width:124px;border-right:1px solid var(--green-dark);color:var(--white);font-size:8px;display:flex;align-items:center;justify-content:center}
.tabs div:last-child{border-right:0}

.intro{text-align:center;color:var(--teal);font-size:13px;line-height:17px;margin:22px auto 0;width:520px}

.topics{display:grid;grid-template-columns:repeat(3,200px);gap:12px 14px;width:628px;margin:24px auto 0}
.topic{height:148px;position:relative}
.topic .thumb{position:absolute;inset:0}
.topic p{position:absolute;left:0;right:0;bottom:0;height:22px;background:var(--teal);color:var(--white);font-size:8px;padding:0 8px;display:flex;align-items:center}

.about{display:flex;justify-content:space-between;width:628px;margin:30px auto 0}
.about h3{font-size:15px;font-weight:400;color:var(--teal);margin-bottom:4px}
.about .sub{font-size:7px;color:var(--muted);border-bottom:1px solid #d3d3cf;padding-bottom:6px;margin-bottom:8px}
.doctor{width:300px}
.doctor .name{font-size:7px;font-weight:600;margin-bottom:6px}
.doc-body{display:flex;gap:10px}
.doc-photo{width:106px;height:82px;border:3px solid var(--white);background:linear-gradient(#e9eef0,#b9c8d0)}
.doc-body p{font-size:7px;line-height:10px;color:var(--muted);flex:1}
.reviews{width:300px}
.review{display:flex;gap:10px}
.avatar{width:28px;height:28px;border-radius:50%;background:#c7ced2;flex:none}
.review p{font-size:7px;line-height:10px;color:var(--muted)}
.review .who{font-size:7px;color:var(--ink);margin-top:4px}
.pager{display:flex;gap:4px;margin:10px 0 0 38px}
.pager i{width:9px;height:9px;background:var(--teal);border-radius:2px}

.footer{position:absolute;left:0;top:992px;width:878px;height:184px;background:var(--footer);color:#cfe0e4}
.footer-cols{display:flex;gap:34px;width:628px;margin:0 auto;padding-top:14px}
.footer h4{color:var(--white);font-size:11px;font-weight:400;padding-bottom:5px;border-bottom:1px solid #4c707a;margin-bottom:8px}
.col{width:130px}
.col p{font-size:7px;line-height:14px;display:flex;gap:5px;align-items:center}
.newsletter{display:flex;margin-top:6px}
.newsletter span{width:80px;height:12px;background:var(--white)}
.newsletter b{background:var(--green);font-size:7px;color:var(--white);padding:0 6px;display:flex;align-items:center;font-weight:600}
.social{display:flex;gap:8px}
.social i{width:10px;height:10px;border-radius:50%;background:#cfe0e4}
.map{width:100px;height:60px;background:linear-gradient(135deg,#dfe3e2,#c4ccc9)}
.to-top{position:absolute;right:128px;bottom:6px;width:18px;height:18px;background:var(--teal);display:flex;align-items:center;justify-content:center}
.bottombar{position:absolute;left:0;top:1176px;width:878px;height:24px;background:var(--footer-deep);color:#a9c0c6;font-size:7px;display:flex;justify-content:space-between;align-items:center;padding:0 130px}
</style>
</head>
<body>

<header class="topbar">
  <div class="brand">DR.MARLOWE</div>
  <div class="top-phone">
    <svg width="10" height="10" viewBox="0 0 24 24"><path fill="#fff" d="M6.6 10.8a15.1 15.1 0 006.6 6.6l2.2-2.2c.3-.3.7-.4 1-.2 1.1.4 2.3.6 3.6.6.6 0 1 .4 1 1V20c0 .6-.4 1-1 1A17 17 0 013 4c0-.6.4-1 1-1h3.5c.6 0 1 .4 1 1 0 1.3.2 2.5.6 3.6.1.3 0 .7-.2 1z"/></svg>
    1 800 555 0142
  </div>
</header>

<section class="hero">
  <div class="hero-photo" role="img" aria-label="Doctor in white coat beside a close-up of a clinician examining a patient's wrist"></div>
  <form class="lead-form">
    <h2>Get a free diagnosis</h2>
    <div class="field"><label>Name</label><span></span></div>
    <div class="field"><label>Phone</label><span></span></div>
    <div class="field"><label>Time</label><span></span></div>
    <div class="field"><label>Email</label><span></span></div>
    <button class="submit" type="button">Submit</button>
  </form>
</section>

<nav class="tabs">
  <div>Carpal Tunnel Syndrome</div>
  <div>Endoscopic Release</div>
  <div>Ganglion Cysts</div>
  <div>Hand Surgery</div>
  <div>Nerve Care</div>
</nav>

<p class="intro">In Dr. Marlowe's clinical practice, Carpal Tunnel Syndrome is one of the most commonly reported health problems</p>

<section class="topics">
  <div class="topic"><div class="thumb" role="img" aria-label="Hand resting on a computer mouse" style="background:linear-gradient(135deg,#7d8f9b,#c9a88f)"></div><p>What is Carpal Tunnel Syndrome</p></div>
  <div class="topic"><div class="thumb" role="img" aria-label="Hands typing on a phone and keyboard" style="background:linear-gradient(135deg,#5f6d78,#a7b4bc)"></div><p>Carpal Tunnel Syndrome and Work Strain</p></div>
  <div class="topic"><div class="thumb" role="img" aria-label="Wrist held in pain" style="background:linear-gradient(135deg,#e7c7ad,#c79775)"></div><p>Endoscopic Release</p></div>
  <div class="topic"><div class="thumb" role="img" aria-label="Close-up of a hand with swollen joints" style="background:linear-gradient(135deg,#c98f7a,#8c5a4c)"></div><p>Ganglion Cysts</p></div>
  <div class="topic"><div class="thumb" role="img" aria-label="Wrist wrapped in a bandage" style="background:linear-gradient(135deg,#55b4b3,#d9b8a4)"></div><p>Hand Surgery</p></div>
  <div class="topic"><div class="thumb" role="img" aria-label="Hand with bandaged fingers" style="background:linear-gradient(135deg,#e5cbb6,#b98e73)"></div><p>Hand Injuries</p></div>
</section>

<section class="about">
  <div class="doctor">
    <h3>Meet Doctor Marlowe</h3>
    <div class="sub">Board certified hand surgeon with years of focused practice</div>
    <div class="name">Dr. Marlowe</div>
    <div class="doc-body">
      <div class="doc-photo" role="img" aria-label="Portrait of the doctor in a white coat"></div>
      <p>Dr. Marlowe has treated thousands of patients with carpal tunnel and related hand conditions. His approach combines careful diagnosis with the least invasive treatment possible, from splinting and therapy to endoscopic release. Patients return to work and daily life quickly with lasting relief from numbness and pain.</p>
    </div>
  </div>
  <div class="reviews">
    <h3>What patients say</h3>
    <div class="sub">Real stories from people who found relief at our clinic</div>
    <div class="review">
      <div class="avatar" role="img" aria-label="Patient avatar"></div>
      <div>
        <p>The numbness in my hand was gone within weeks of the procedure. The team explained every step and made me feel at ease. I can type and sleep again without pain.</p>
        <div class="who">Patient</div>
      </div>
    </div>
    <div class="pager"><i></i><i></i></div>
  </div>
</section>

<footer class="footer">
  <div class="footer-cols">
    <div class="col">
      <h4>Contact Us</h4>
      <p>
        <svg width="8" height="8" viewBox="0 0 24 24"><path fill="#cfe0e4" d="M12 2a7 7 0 00-7 7c0 5 7 13 7 13s7-8 7-13a7 7 0 00-7-7zm0 9.5A2.5 2.5 0 1112 6a2.5 2.5 0 010 5.5z"/></svg>
        214 Harbor Lane, Suite 300, Westfield
      </p>
      <p>
        <svg width="8" height="8" viewBox="0 0 24 24"><path fill="#cfe0e4" d="M6.6 10.8a15.1 15.1 0 006.6 6.6l2.2-2.2c.3-.3.7-.4 1-.2 1.1.4 2.3.6 3.6.6.6 0 1 .4 1 1V20c0 .6-.4 1-1 1A17 17 0 013 4c0-.6.4-1 1-1h3.5c.6 0 1 .4 1 1 0 1.3.2 2.5.6 3.6.1.3 0 .7-.2 1z"/></svg>
        1 800 555 0142
      </p>
      <p>
        <svg width="8" height="8" viewBox="0 0 24 24"><path fill="#cfe0e4" d="M3 5h18v14H3zm2 2v.5l7 4.5 7-4.5V7z"/></svg>
        info@drmarlowe.example
      </p>
      <p>Monday – Friday: 8:00 am – 5:00 pm</p>
      <p>Saturday: 9:00 am – 1:00 pm</p>
    </div>
    <div class="col">
      <h4>Newsletter</h4>
      <p>Subscribe for hand health tips and clinic news.</p>
      <div class="newsletter"><span></span><b>Subscribe</b></div>
    </div>
    <div class="col">
      <h4>Connect Us</h4>
      <div class="social"><i></i><i></i><i></i><i></i></div>
    </div>
    <div class="col">
      <h4>Locate Us</h4>
      <div class="map" role="img" aria-label="Street map showing the clinic location"></div>
    </div>
  </div>
  <div class="to-top">
    <svg width="8" height="8" viewBox="0 0 10 10"><path d="M1 7l4-4 4 4" stroke="#fff" stroke-width="1.6" fill="none"/></svg>
  </div>
</footer>

<div class="bottombar">
  <span>© Copyright Dr. Marlowe. All rights reserved</span>
  <span>Designed for Dr. Marlowe</span>
</div>

</body>
</html>
```